Poster Design Project

Poster with modern feeling to be displayed in office. The text that needs to be included in this poster is below:

Rules
1. If it’s not in writing it doesn’t exist.
2. No such thing as 'off the record.'
3. Do not hold a private conversation in a public place.
4. Don’t believe any number that ends in zero.
5. Never turn down an opportunity to eat or go to the bathroom.
6. Don’t spend any of your own money. Don’t even admit you own a credit card. Don’t spend money that is not yours.
7. Not always a 'right' or 'wrong' answer - 'It depends.'
8. In a campaign, someone has to be in charge – campaigns are a place to foster democracy, not practice it.
9. Assume nothing.
10. If you make a mistake, fix it before analyzing. Bad news doesn’t age well.

Industry/Entity Type

Credit Card

Requirements
Must have
• Rules
7. Not always a “right” or “wrong” answer - 'It depends.' 
9. Assume nothing.

```html
<!DOCTYPE html>
<html lang="en">
<head>
<meta charset="utf-8">
<title>Office Rules Poster Series</title>
<link href="https://fonts.googleapis.com/css2?family=Marck+Script&family=Open+Sans:ital,wght@0,400;0,600;0,700;1,700&display=swap" rel="stylesheet">
<style>
  :root {
    --board: #432b24;
    --paper: #ffffff;
    --red: #d9261c;
    --ink: #111111;
    --ink-soft: #3a1512;
    --slate: #3b3e40;
    --frame: #d4a45a;
    --chalk: #f2f2f2;
    --note: #e8dcd6;
    --script: "Marck Script", cursive;
    --sans: "Open Sans", sans-serif;
  }
  * { margin: 0; padding: 0; box-sizing: border-box; }
  html, body { width: 848px; height: 1200px; overflow: hidden; }
  body { background: var(--board); font-family: var(--sans); position: relative; }

  .poster { position: absolute; background: var(--paper); overflow: hidden; }
  .rule-label { position: absolute; font-family: var(--script); color: var(--ink); font-size: 50px; line-height: 1; white-space: nowrap; }

  /* Rule 1 */
  .poster--one { left: 43px; top: 68px; width: 363px; height: 514px; }
  .notepad-photo { position: absolute; left: 0; top: 0; width: 300px; height: 480px;
    background: linear-gradient(160deg, #fafafa 0%, #e9e9e9 55%, #d8d8d8 100%); }
  .poster--one .rule-label { left: 44px; top: 126px; font-size: 46px; transform: rotate(-10deg); transform-origin: left bottom; }
  .writing-box { position: absolute; left: 180px; top: 111px; width: 183px; height: 331px;
    background: var(--red); color: var(--paper); font-style: italic; font-weight: 700;
    padding: 50px 0 0 16px; line-height: 1; letter-spacing: -0.5px; }
  .writing-box .sm { display: block; font-size: 25px; margin-bottom: 12px; }
  .writing-box .md { display: block; font-size: 42px; margin-bottom: 14px; }
  .writing-box .lg { display: block; font-size: 60px; }

  /* Rule 2 */
  .poster--two { left: 437px; top: 68px; width: 364px; height: 514px; }
  .poster--two .rule-label { left: 12px; top: 38px; }
  .ledger-photo { position: absolute; left: 0; top: 108px; width: 348px; height: 296px;
    background: linear-gradient(120deg, #8a7058 0%, #c9b191 40%, #e1cfb2 70%, #a88e70 100%); }
  .record-band { position: absolute; left: 156px; top: 0; width: 157px; height: 514px; background: var(--red);
    padding: 126px 0 0 6px; font-weight: 700; line-height: 1; letter-spacing: -1px; }
  .record-band span { display: block; }
  .record-band .no { font-size: 42px; color: var(--ink); }
  .record-band .soft { font-size: 26px; font-weight: 400; color: var(--ink-soft); }
  .record-band .off { font-size: 54px; color: var(--paper); margin-top: -2px; }
  .record-band .the { font-size: 22px; color: var(--paper); }
  .record-band .record { font-size: 36px; color: var(--paper); }

  /* Rule 3 */
  .poster--three { left: 43px; top: 615px; width: 367px; height: 515px; }
  .poster--three .red-field { position: absolute; left: 0; top: 166px; width: 100%; height: 349px; background: var(--red); }
  .poster--three .rule-label { left: 15px; top: 30px; }
  .bubbles { position: absolute; left: 0; top: 0; }
  .bubbles text { font-family: var(--sans); fill: var(--paper); letter-spacing: -1px; }

  /* Rule 4 */
  .poster--four { left: 444px; top: 621px; width: 361px; height: 509px; }
  .red-band { position: absolute; left: 103px; top: 0; width: 159px; height: 100%; background: var(--red); }
  .poster--four .rule-label { left: 122px; top: 14px; color: var(--paper); font-size: 48px; }
  .chalkboard { position: absolute; left: 0; top: 74px; width: 361px; height: 365px;
    background: var(--slate); border: 6px solid var(--frame); box-shadow: 0 10px 14px rgba(0,0,0,0.35);
    color: var(--chalk); text-align: center; padding-top: 72px; line-height: 1; }
  .chalkboard p { white-space: nowrap; }
  .chalkboard .big { font-weight: 600; }
  .chalkboard .line1 { font-size: 30px; }
  .chalkboard .line1 .big { font-size: 46px; }
  .chalkboard .line2 { font-size: 22px; margin-top: 4px; }
  .chalkboard .line2 .big { font-size: 36px; }
  .chalkboard .line3 { font-size: 22px; margin-top: 10px; }
  .chalkboard .line3 .big { font-size: 36px; }
  .chalkboard .zero { font-size: 96px; margin-top: -6px; }

  /* More rules */
  .more-rules { position: absolute; left: 43px; top: 1146px; width: 762px; display: flex; justify-content: space-between;
    color: var(--note); font-size: 14px; line-height: 1.3; white-space: nowrap; }
  .more-rules strong { font-family: var(--script); font-weight: 400; font-size: 22px; color: var(--paper); margin-right: 6px; }
</style>
</head>
<body>

<section class="poster poster--one">
  <div class="notepad-photo" role="img" aria-label="Photo of a lined notepad with a yellow pencil"></div>
  <div class="rule-label">Rule 1</div>
  <div class="writing-box">
    <span class="sm">If it’s not in</span>
    <span class="md">writing</span>
    <span class="sm">it doesn’t</span>
    <span class="lg">exist</span>
  </div>
</section>

<section class="poster poster--two">
  <div class="rule-label">Rule 2</div>
  <div class="ledger-photo" role="img" aria-label="Photo of an open old handwritten ledger"></div>
  <div class="record-band">
    <span class="no">No</span>
    <span class="soft">such</span>
    <span class="soft">thing</span>
    <span class="soft">as</span>
    <span class="off">off</span>
    <span class="the">the</span>
    <span class="record">record</span>
  </div>
</section>

<section class="poster poster--three">
  <div class="red-field"></div>
  <div class="rule-label">Rule 3</div>
  <svg class="bubbles" width="367" height="515" viewBox="0 0 367 515">
    <path d="M70 350 C60 280 150 250 220 255 C300 258 335 300 320 345 C305 395 230 410 170 400 L110 410 L130 385 C95 375 75 365 70 350 Z" fill="#111"/>
    <path d="M155 150 C150 105 200 82 250 85 C305 88 345 118 340 160 C338 190 320 205 305 212 L345 270 L290 222 C270 228 235 228 205 218 C175 205 157 182 155 150 Z" fill="#111"/>
    <path d="M12 235 C8 190 60 162 120 162 C185 162 235 195 232 238 C230 280 180 305 125 305 L60 335 L75 300 C35 290 14 265 12 235 Z" fill="#111" stroke="#d9261c" stroke-width="4"/>
    <path d="M170 312 C168 270 210 245 258 245 C310 245 350 275 348 318 C346 360 305 385 258 383 C230 382 210 375 195 368 L165 385 L180 355 C172 342 170 328 170 312 Z" fill="#111"/>
    <text x="212" y="158" font-size="46" font-weight="400">Do</text>
    <text x="236" y="188" font-size="28">not</text>
    <text x="78" y="206" font-size="30">hold <tspan font-size="20">a</tspan></text>
    <text x="30" y="252" font-size="46">private</text>
    <text x="52" y="285" font-size="22">conversation</text>
    <text x="228" y="272" font-size="21">in<tspan font-size="14">a</tspan></text>
    <text x="196" y="318" font-size="42">public</text>
    <text x="218" y="356" font-size="30">place</text>
  </svg>
</section>

<section class="poster poster--four">
  <div class="red-band"></div>
  <div class="rule-label">Rule 4</div>
  <div class="chalkboard">
    <p class="line1"><span class="big">Don’t</span> believe</p>
    <p class="line2">any <span class="big">number</span></p>
    <p class="line3">that <span class="big">ends</span> in</p>
    <p class="zero">zero</p>
  </div>
</section>

<footer class="more-rules">
  <p><strong>Rule 7</strong>Not always a “right” or “wrong” answer – ‘It depends.’</p>
  <p><strong>Rule 9</strong>Assume nothing.</p>
</footer>

</body>
</html>
```